Business Card Design

I am a Special Event Consultant,I arrange and organise Special Events - Product Launches,Sponsorship and Product Displays.

I would like the RTV to be a feature of the design with 'Special Event Services" underneath - keep it very simple but creative using this information. So it is just the letters "RTV" with Event Services underneath.

(Simple Colours - Silver, Black, Grey - no bright colours - We work for Valtoria Drenn,KDX, Lyndrel So it is class and classic.)

Only my Name and mobile on the front.

Contact Information for Business Card

FRONT
Tess Varnholt
Tel: 0436 218907

BACK
Email: tess@rtveventservices.example.au

2807 Wexbury Heights,83 Pollard Street
NORTHVALE.Vic.3158.

```html
<!DOCTYPE html>
<html lang="en">
<head>
<meta charset="utf-8">
<title>RTV Special Event Services – Business Card</title>
<link rel="stylesheet" href="https://fonts.googleapis.com/css2?family=Cinzel:wght@400;500&display=swap">
<style>
  :root {
    --backdrop: #e6e6e8;
    --card-charcoal: #4b4d53;
    --band-silver: #a9a9ab;
    --band-silver-light: #b4b4b6;
    --ink-dark: #55575d;
    --ink-light: #c9c9cc;
    --brand-silver: #8e8f93;
  }
  * { box-sizing: border-box; margin: 0; padding: 0; }
  html, body {
    width: 1200px;
    height: 900px;
    overflow: hidden;
    background: var(--backdrop);
    font-family: "Cinzel", "Times New Roman", serif;
  }
  .card {
    position: absolute;
    top: 292px;
    width: 520px;
    height: 316px;
    border-radius: 20px;
    background: var(--card-charcoal);
    overflow: hidden;
  }
  .card--back { left: 50px; }
  .card--front { left: 630px; }

  .band { position: absolute; left: 0; width: 100%; background: var(--band-silver); }
  .band--light { background: var(--band-silver-light); }

  /* back side */
  .card--back .band-top { top: 44px; height: 26px; }
  .card--back .band-main { top: 84px; height: 116px; }
  .card--back .band-contact { top: 214px; height: 22px; }

  .brand-mark {
    position: absolute;
    left: 26px;
    top: 18px;
    font-size: 66px;
    font-weight: 500;
    line-height: 1;
    color: var(--brand-silver);
    letter-spacing: 2px;
  }
  .brand-tagline {
    position: absolute;
    left: 26px;
    top: 128px;
    font-size: 33px;
    font-weight: 400;
    color: var(--ink-dark);
    letter-spacing: 1px;
    white-space: nowrap;
  }
  .contact-email {
    position: absolute;
    left: 28px;
    top: 217px;
    font-size: 13.5px;
    color: var(--ink-dark);
    white-space: nowrap;
  }
  .contact-address {
    position: absolute;
    left: 18px;
    top: 248px;
    font-size: 14px;
    line-height: 1.45;
    color: var(--ink-light);
  }

  /* front side */
  .card--front .band-top { top: 26px; height: 24px; }
  .card--front .band-main { top: 62px; height: 118px; }
  .card--front .band-under { top: 192px; height: 20px; }

  .holder-name {
    position: absolute;
    left: 0;
    width: 100%;
    top: 96px;
    text-align: center;
    font-size: 44px;
    font-weight: 400;
    color: var(--ink-dark);
    letter-spacing: 2px;
    white-space: nowrap;
  }
  .holder-phone {
    position: absolute;
    left: 0;
    width: 100%;
    top: 238px;
    text-align: center;
    font-size: 28px;
    color: var(--ink-light);
    letter-spacing: 1.5px;
  }
</style>
</head>
<body>
  <section class="card card--back" aria-label="Business card back">
    <div class="band band-top band--light"></div>
    <div class="band band-main"></div>
    <div class="band band-contact band--light"></div>
    <div class="brand-mark">RTV</div>
    <h1 class="brand-tagline">Special Event Services</h1>
    <p class="contact-email">Email: tess@rtveventservices.example.au</p>
    <p class="contact-address">2807 Wexbury Heights,83 Pollard Street NORTHVALE.<br>Vic.3158.</p>
  </section>

  <section class="card card--front" aria-label="Business card front">
    <div class="band band-top band--light"></div>
    <div class="band band-main"></div>
    <div class="band band-under band--light"></div>
    <h2 class="holder-name">Tess Varnholt</h2>
    <p class="holder-phone">Tel: 0436 218907</p>
  </section>
</body>
</html>
```